UX - Need some screens design for a Skill Assessment Application

I am building an app to carry out skill assessments. Depending on how the assessment is configured, it may have one or more parts
1. Question based assessment (Multiple Choice, True False, Fill in the blanks"
2. Endorsement by two colleagues - A screen that allows user to pick colleagues based on search and shows the status of pending requests
3. A written submission - a page that explains the format of the submission and a file upload
As each assessment can be configured with or without any of the steps, the assessment UI must be such that these areas get hidden/displayed based on configuration.
Colour codes to be used can be #0e78bb and #ffffff
There will also be a start screen (instructions) and an end screen (results)
Target Market(s)
Enterprise software
Number of Pages Required
4 page

```html
<!DOCTYPE html>
<html lang="en">
<head>
<meta charset="utf-8">
<title>Veranth – Skill Assessment Screens</title>
<link href="https://fonts.googleapis.com/css2?family=Inter:wght@400;500;600;700&display=swap" rel="stylesheet">
<style>
:root{
  --bg:#2a2a2a;
  --brand:#0756b0;
  --brand-card:#1b67bd;
  --accent:#0e78bb;
  --teal:#1b9c9c;
  --ink:#1f2329;
  --muted:#6b7280;
  --line:#e3e6ea;
  --band:#e8edf2;
  --page:#f3f4f6;
  --chip:#eceef1;
  --white:#ffffff;
  --toast:#22a07a;
}
*{box-sizing:border-box;margin:0;padding:0}
html,body{width:1032px;height:1200px;overflow:hidden;background:var(--bg);font-family:'Inter',sans-serif;color:var(--ink)}
.board{position:relative;width:1032px;height:1200px;overflow:hidden}
.step-no{position:absolute;color:var(--white);font-weight:600;font-size:16px;line-height:1}
.screen{position:absolute;width:712px;height:457px;background:var(--white);transform:scale(.5792);transform-origin:0 0;overflow:hidden}

/* navigation */
.nav{position:absolute;top:0;left:0;right:0;height:26px;background:var(--brand);display:flex;align-items:center;padding:0 42px;color:var(--white);font-size:7px}
.brand{display:flex;align-items:center;gap:5px;font-weight:600;font-size:7.5px;width:200px}
.brand-dot{width:11px;height:11px;border-radius:50%;background:var(--white)}
.links{display:flex;gap:12px;margin-left:48px;height:26px}
.links a{display:flex;align-items:center;color:rgba(255,255,255,.8);font-size:6.5px;border-bottom:2px solid transparent}
.links a.on{color:var(--white);font-weight:600;border-bottom-color:#7fc2ff}
.nav-icons{margin-left:auto;display:flex;align-items:center;gap:11px;padding-right:16px}
.nav-icons svg{width:9px;height:9px}
.avatar{display:inline-block;border-radius:50%;background:radial-gradient(circle at 45% 40%,#c99b80,#5b4032 70%);flex:none}
.avatar.sm{width:14px;height:14px}
.avatar.lg{width:26px;height:26px}
.avatar.row{width:12px;height:12px}

/* dashboard */
.hero{position:absolute;top:26px;left:0;right:0;height:145px;background:var(--brand);padding:16px 34px 0;color:var(--white)}
.welcome{display:flex;align-items:center;gap:11px;height:26px}
.hello{font-size:6.5px;opacity:.75}
.who{font-size:10px;font-weight:600;margin-top:2px}
.btn-create{margin-left:auto;height:19px;padding:0 8px;background:var(--accent);border:1px solid #3b98d6;border-radius:2px;display:flex;align-items:center;gap:5px;font-size:6.3px;font-weight:500}
.btn-create svg{width:7px;height:7px}
.summary{font-size:7.5px;margin-top:20px}
.stats{display:grid;grid-template-columns:repeat(4,154px);gap:9px;margin-top:7px}
.stat{height:52px;background:var(--brand-card);border-radius:2px;padding:10px 12px;display:flex;gap:12px}
.stat svg{width:16px;height:16px;flex:none}
.stat b{display:block;font-size:10px;font-weight:600}
.stat span{display:block;font-size:7px;margin-top:3px}
.stat small{display:block;font-size:4.8px;opacity:.75;margin-top:2px}
.list-area{position:absolute;top:171px;left:0;right:0;bottom:0;background:var(--page);padding:18px 42px}
.list-area h2{font-size:9.5px;font-weight:600}
.toolbar{display:flex;align-items:center;margin-top:8px;height:19px}
.tabs{display:flex}
.tab{height:19px;padding:0 10px;display:flex;align-items:center;font-size:6.3px;background:#e2e5e9;color:var(--muted)}
.tab.on{background:var(--accent);color:var(--white);font-weight:500}
.views{margin-left:auto;display:flex;gap:10px;padding-right:6px}
.views svg{width:10px;height:10px}
.cards{display:grid;grid-template-columns:repeat(3,201px);column-gap:12px;row-gap:11px;margin-top:11px}
.card{position:relative;height:100px;background:var(--white);padding:11px 12px;border-radius:2px}
.card-id{font-size:7px;display:flex;justify-content:space-between}
.kebab{font-size:9px;font-weight:700;line-height:7px}
.card-title{font-size:7px;color:var(--accent);margin-top:5px}
.dates{display:grid;grid-template-columns:75px 75px;margin-top:8px}
.dates small{display:block;font-size:4.6px;text-transform:uppercase;color:var(--ink)}
.dates span{display:block;font-size:7px;color:#444;margin-top:2px}
.chips{display:flex;gap:5px;margin-top:12px}
.chip{display:flex;align-items:center;gap:3px;height:11px;padding:0 6px;border-radius:6px;background:var(--chip);font-size:5.8px;color:#555}
.chip.done::after{content:"✓";width:7px;height:7px;border-radius:50%;background:var(--teal);color:var(--white);font-size:4.5px;display:flex;align-items:center;justify-content:center}
.menu{position:absolute;right:12px;top:4px;width:52px;background:#5d5d5d;border-radius:2px;padding:4px 6px;color:var(--white);font-size:6.3px;text-align:right;line-height:13px}
.toast{position:absolute;top:30px;left:259px;width:195px;height:20px;background:var(--toast);border-radius:2px;color:var(--white);font-size:5.8px;display:flex;align-items:center;justify-content:center;gap:5px;z-index:2}
.toast i{width:8px;height:8px;border-radius:50%;background:var(--white);color:var(--toast);font-style:normal;font-size:5px;display:flex;align-items:center;justify-content:center}

/* assessment flow */
.crumb{position:absolute;top:39px;left:34px;display:flex;align-items:center;gap:6px;font-size:6px;color:#555}
.crumb a{color:var(--accent)}
.crumb svg{width:10px;height:10px}
.a-title{position:absolute;top:57px;left:52px;display:flex;align-items:center;gap:9px;font-size:12.5px;font-weight:500}
.a-title svg{width:12px;height:12px}
.pct{position:absolute;top:55px;right:52px;font-size:17px;font-weight:700}
.pct small{font-size:8px;font-weight:500}
.progress{position:absolute;top:84px;left:0;right:0;height:3px;background:#dfe3e8}
.progress i{display:block;height:3px;background:var(--teal)}
.meta{position:absolute;top:87px;left:0;right:0;height:26px;background:var(--band);display:flex;align-items:center;padding:0 52px;gap:26px;font-size:5.6px;color:#444}
.meta a{color:var(--accent)}
.meta .upd{margin-left:auto}
.steps{position:absolute;top:150px;left:48px;font-size:7.5px}
.steps li{list-style:none;display:flex;align-items:center;gap:8px;height:27px}
.steps .mark{width:8px;height:8px;border-radius:50%;border:1px solid #c7ccd2}
.steps .done{color:var(--teal)}
.steps .done .mark{background:var(--teal);border-color:var(--teal);color:var(--white);font-size:5px;display:flex;align-items:center;justify-content:center}
.section-head{position:absolute;top:129px;left:217px;width:443px;height:22px;border-bottom:1px solid var(--line);display:flex;align-items:center}
.section-head h3{font-size:8.5px;font-weight:600}
.save{margin-left:auto;display:flex;align-items:center;gap:5px;font-size:6px;color:var(--accent)}
.save svg{width:8px;height:8px}
.filters{position:absolute;top:162px;left:217px;display:flex;gap:6px}
.field{height:18px;border:1px solid var(--line);border-radius:2px;display:flex;align-items:center;padding:0 7px;font-size:5.8px;color:#888}
.field svg{width:7px;height:7px;margin-left:auto}
.select{width:116px;color:#333}
.search{width:92px}
.send{width:58px;color:#aaa}
.people{position:absolute;top:188px;left:217px;width:278px}
.person{height:23px;margin-bottom:3.5px;border:1px solid #edf0f3;border-radius:2px;display:flex;align-items:center;padding:0 3px;gap:6px;font-size:6.5px}
.check{width:7px;height:7px;border:1px solid #d5d9de;border-radius:1px}
.person .role{margin-left:auto;font-size:5.3px;color:#666;margin-right:14px}
.btn-add{width:22px;height:12px;background:var(--accent);color:var(--white);font-size:5.8px;border-radius:2px;display:flex;align-items:center;justify-content:center}
.btn-cancel{width:30px;height:12px;border:1px solid var(--accent);color:var(--accent);font-size:5.8px;border-radius:2px;display:flex;align-items:center;justify-content:center}
.note{position:absolute;top:162px;left:532px;width:128px;height:100px;background:var(--page);padding:12px}
.note h4{font-size:8.5px;font-weight:500}
.note p{font-size:5.6px;line-height:9.5px;color:#666;margin-top:6px}
.pager{position:absolute;top:384px;left:284px;display:flex;align-items:center;gap:9px;font-size:6px}
.pg{height:18px;display:flex;align-items:center;justify-content:center;border-radius:2px}
.pg.prev{width:49px;border:1px solid var(--line);color:#bbb}
.pg.cur{width:19px;background:var(--accent);color:var(--white)}
.pg.next{width:38px;background:var(--accent);color:var(--white)}
.foot{position:absolute;top:420px;left:0;right:0;bottom:0;border-top:1px solid var(--line)}
.btn-back{position:absolute;top:10px;left:52px;width:43px;height:18px;border:1px solid var(--accent);color:var(--accent);border-radius:2px;font-size:6px;display:flex;align-items:center;justify-content:center}
.skip{position:absolute;top:15px;left:594px;font-size:6px;color:#555}
.btn-next{position:absolute;top:10px;right:52px;height:18px;padding:0 9px;background:var(--accent);color:var(--white);border-radius:2px;font-size:6px;display:flex;align-items:center}
.veil{position:absolute;inset:0;background:rgba(60,60,60,.32);z-index:3}
.modal{position:absolute;top:147px;left:264px;width:185px;height:164px;background:var(--white);border-radius:6px;padding:12px 16px;z-index:4}
.modal h4{font-size:8.5px;font-weight:600;padding-bottom:7px;border-bottom:1px solid var(--line)}
.modal .avatar{margin-top:8px}
.modal p{font-size:5.6px;color:#555;margin-top:7px}
.modal label{display:block;font-size:5px;margin-top:10px;color:#444}
.modal .field{margin-top:4px;color:#333}
.modal-actions{display:flex;justify-content:space-between;margin-top:15px}
.modal-actions span{height:16px;padding:0 9px;display:flex;align-items:center;font-size:5.8px;border-radius:2px}
.m-cancel{border:1px solid var(--accent);color:var(--accent)}
.m-submit{background:var(--accent);color:var(--white)}
</style>
</head>
<body>
<main class="board">

<span class="step-no" style="left:274px;top:39px">1</span>
<span class="step-no" style="left:50px;top:334px">2</span>
<span class="step-no" style="left:540px;top:334px">3</span>
<span class="step-no" style="left:50px;top:614px">4</span>
<span class="step-no" style="left:540px;top:614px">5</span>
<span class="step-no" style="left:50px;top:894px">6</span>
<span class="step-no" style="left:540px;top:894px">7</span>

<!-- Screen 1: dashboard, pending -->
<section class="screen" style="left:304.6px;top:37px">
  <header class="nav"><span class="brand"><i class="brand-dot"></i>Veranth</span><nav class="links"><a class="on">Assessments</a><a>Colleagues</a><a>Results</a></nav><span class="nav-icons"><svg viewBox="0 0 10 10" fill="none" stroke="#fff"><path d="M2.5 7V4.5a2.5 2.5 0 0 1 5 0V7l1 1h-7zM4 9h2"/></svg><svg viewBox="0 0 10 10" fill="none" stroke="#fff"><circle cx="5" cy="5" r="3.5"/><circle cx="5" cy="5" r="1.3"/></svg><span class="avatar sm" role="img" aria-label="Profile photo of Mara T. Solvang"></span></span></header>
  <div class="hero">
    <div class="welcome"><span class="avatar lg" role="img" aria-label="Profile photo of Mara T. Solvang"></span><div><p class="hello">Welcome back!</p><p class="who">Mara T. Solvang</p></div><span class="btn-create"><svg viewBox="0 0 8 8" fill="none" stroke="#fff"><rect x="1" y="1" width="6" height="6"/></svg>Create New Assessment</span></div>
    <p class="summary">Summary</p>
    <div class="stats">
      <div class="stat"><svg viewBox="0 0 16 16" fill="none" stroke="#fff"><rect x="2.5" y="1.5" width="10" height="13" rx="1"/><path d="M5 5h5M5 8h3"/><circle cx="10.5" cy="11" r="2"/></svg><div><b>7</b><span>My Assessments</span><small>3 pending</small></div></div>
      <div class="stat"><svg viewBox="0 0 16 16" fill="none" stroke="#fff"><path d="M2 14h12M4 14V9h3l2 2h3v3M8 2v4M6 4l2-2 2 2"/></svg><div><b>3</b><span>Endorsements</span><small>1 pending</small></div></div>
      <div class="stat"><svg viewBox="0 0 16 16" fill="none" stroke="#fff"><circle cx="5.5" cy="5" r="2"/><circle cx="10.5" cy="5" r="2"/><path d="M2 13c0-3 7-3 7 0M7 13c0-3 7-3 7 0"/></svg><div><b>10</b><span>Colleagues</span><small>Last updated on May 23, 2024</small></div></div>
      <div class="stat"><svg viewBox="0 0 16 16" fill="none" stroke="#fff"><path d="M2 9v5h12V9M8 2v8M5 5l3-3 3 3"/></svg><div><b>7</b><span>Submissions</span><small>Last submit on May 23, 2024</small></div></div>
    </div>
  </div>
  <div class="list-area">
    <h2>Assessments</h2>
    <div class="toolbar"><div class="tabs"><span class="tab on">Pending 3</span><span class="tab">Completed 4</span></div><span class="views"><svg viewBox="0 0 10 10" fill="none" stroke="#0e78bb"><path d="M1 2h1M3.5 2H9M1 5h1M3.5 5H9M1 8h1M3.5 8H9"/></svg><svg viewBox="0 0 10 10" fill="none" stroke="#888"><rect x="1" y="1" width="3.3" height="3.3"/><rect x="5.7" y="1" width="3.3" height="3.3"/><rect x="1" y="5.7" width="3.3" height="3.3"/><rect x="5.7" y="5.7" width="3.3" height="3.3"/></svg></span></div>
    <div class="cards">
      <article class="card"><div class="card-id">1723091983<span class="kebab">⋮</span></div><p class="card-title">Application Design Capabilities</p><div class="dates"><div><small>Published on</small><span>20/05/2024</span></div><div><small>Due date</small><span>24/05/2024</span></div></div><div class="chips"><span class="chip">Quiz</span><span class="chip">Endorsement</span><span class="chip">Submission</span></div></article>
      <article class="card"><div class="card-id">1723091983<span class="kebab">⋮</span></div><p class="card-title">UI/UX Designer Assessments</p><div class="dates"><div><small>Published on</small><span>20/05/2024</span></div><div><small>Due date</small><span>24/05/2024</span></div></div><div class="chips"><span class="chip done">Quiz</span><span class="chip">Endorsement</span></div></article>
      <article class="card"><div class="card-id">1723091983<span class="kebab">⋮</span></div><p class="card-title">Sales Representative Assessments</p><div class="dates"><div><small>Published on</small><span>20/05/2024</span></div><div><small>Due date</small><span>24/05/2024</span></div></div><div class="chips"><span class="chip done">Quiz</span><span class="chip done">Endorsement</span><span class="chip">Submission</span></div></article>
    </div>
  </div>
</section>

<!-- Screen 2: endorsement step -->
<section class="screen" style="left:78px;top:332px">
  <header class="nav"><span class="brand"><i class="brand-dot"></i>Veranth</span><nav class="links"><a class="on">Assessments</a><a>Colleagues</a><a>Results</a></nav><span class="nav-icons"><svg viewBox="0 0 10 10" fill="none" stroke="#fff"><path d="M2.5 7V4.5a2.5 2.5 0 0 1 5 0V7l1 1h-7zM4 9h2"/></svg><svg viewBox="0 0 10 10" fill="none" stroke="#fff"><circle cx="5" cy="5" r="3.5"/><circle cx="5" cy="5" r="1.3"/></svg><span class="avatar sm" role="img" aria-label="Profile photo of Mara T. Solvang"></span></span></header>
  <div class="crumb"><svg viewBox="0 0 10 10" fill="none" stroke="#0e78bb"><circle cx="5" cy="5" r="4.3"/><path d="M5.5 3 3.5 5l2 2M3.5 5H7"/></svg><a>Assessment</a>/<span>Application Design Capabilities</span></div>
  <h1 class="a-title"><svg viewBox="0 0 12 12" fill="none" stroke="#333"><rect x="1.5" y="1" width="8" height="10" rx="1"/><path d="M3.5 4h4M3.5 6.5h2"/></svg>UI/UX Designer Assessment</h1>
  <p class="pct">80<small>%</small></p>
  <div class="progress"><i style="width:76%"></i></div>
  <div class="meta"><span>Assessment Date: <a>Feb 12, 2024</a></span><span>Assessment Type: <a>UI/UX Skill</a></span><span>Due Date: 17/02/2024</span><span class="upd">Last Updated: 23/05/2024</span></div>
  <ul class="steps"><li class="done"><span class="mark">✓</span>Quiz</li><li><span class="mark"></span>Endorsement</li></ul>
  <div class="section-head"><h3>Endorsement</h3><span class="save"><svg viewBox="0 0 8 8" fill="none" stroke="#0e78bb"><rect x="1" y="1" width="6" height="6"/><path d="M2.5 1v2h3V1"/></svg>Save Progress</span></div>
  <div class="filters"><span class="field select">All categories<svg viewBox="0 0 8 8" fill="none" stroke="#333"><path d="M2 3l2 2 2-2"/></svg></span><span class="field search">Search<svg viewBox="0 0 8 8" fill="none" stroke="#555"><circle cx="3.5" cy="3.5" r="2.5"/><path d="M5.3 5.3 7 7"/></svg></span><span class="field send">Send Request</span></div>
  <div class="people">
    <div class="person"><i class="check"></i><span class="avatar row" role="img" aria-label="Photo of Lena Ostrova"></span>Lena Ostrova<span class="role">Application Design Capabilities</span><span class="btn-add">Add</span></div>
    <div class="person"><i class="check"></i><span class="avatar row" role="img" aria-label="Photo of Owen Hartley"></span>Owen Hartley<span class="role">UI/UX Designer</span><span class="btn-add">Add</span></div>
    <div class="person"><i class="check"></i><span class="avatar row" role="img" aria-label="Photo of Paul Navarro"></span>Paul Navarro<span class="role">Front-end Developer</span><span class="btn-add">Add</span></div>
    <div class="person"><i class="check"></i><span class="avatar row" role="img" aria-label="Photo of Nora Lindqvist"></span>Nora Lindqvist<span class="role">Cybersecurity Analyst</span><span class="btn-add">Add</span></div>
    <div class="person"><i class="check"></i><span class="avatar row" role="img" aria-label="Photo of Simon Avery"></span>Simon Avery<span class="role">DevOps Engineer</span><span class="btn-add">Add</span></div>
    <div class="person"><i class="check"></i><span class="avatar row" role="img" aria-label="Photo of Tessa Morrow"></span>Tessa Morrow<span class="role">DevOps Engineer</span><span class="btn-add">Add</span></div>
    <div class="person"><i class="check"></i><span class="avatar row" role="img" aria-label="Photo of Ivan Beckett"></span>Ivan Beckett<span class="role">DevOps Engineer</span><span class="btn-add">Add</span></div>
  </div>
  <aside class="note"><h4>Note</h4><p>Lorem ipsum dolor sit amet, consecteteur adispiscing elit. Lorem ipsum dolor sit amet, consecteteur adispiscing elit.Lorem ipsum dolor.</p></aside>
  <div class="pager"><span class="pg prev">‹ Previous</span><span class="pg cur">1</span><span>2</span><span class="pg next">Next ›</span></div>
  <footer class="foot"><span class="btn-back">Go Back</span><span class="skip">Skip ›</span><span class="btn-next">Next</span></footer>
</section>

<!-- Screen 3: endorsement confirm dialog -->
<section class="screen" style="left:568.6px;top:332px">
  <header class="nav"><span class="brand"><i class="brand-dot"></i>Veranth</span><nav class="links"><a class="on">Assessments</a><a>Colleagues</a><a>Results</a></nav><span class="nav-icons"><svg viewBox="0 0 10 10" fill="none" stroke="#fff"><path d="M2.5 7V4.5a2.5 2.5 0 0 1 5 0V7l1 1h-7zM4 9h2"/></svg><svg viewBox="0 0 10 10" fill="none" stroke="#fff"><circle cx="5" cy="5" r="3.5"/><circle cx="5" cy="5" r="1.3"/></svg><span class="avatar sm" role="img" aria-label="Profile photo of Mara T. Solvang"></span></span></header>
  <div class="crumb"><svg viewBox="0 0 10 10" fill="none" stroke="#0e78bb"><circle cx="5" cy="5" r="4.3"/><path d="M5.5 3 3.5 5l2 2M3.5 5H7"/></svg><a>Assessment</a>/<span>Application Design Capabilities</span></div>
  <h1 class="a-title"><svg viewBox="0 0 12 12" fill="none" stroke="#333"><rect x="1.5" y="1" width="8" height="10" rx="1"/><path d="M3.5 4h4M3.5 6.5h2"/></svg>UI/UX Designer Assessment</h1>
  <p class="pct">80<small>%</small></p>
  <div class="progress"><i style="width:76%"></i></div>
  <div class="meta"><span>Assessment Date: <a>Feb 12, 2024</a></span><span>Assessment Type: <a>UI/UX Skill</a></span><span>Due Date: 17/02/2024</span><span class="upd">Last Updated: 23/05/2024</span></div>
  <ul class="steps"><li class="done"><span class="mark">✓</span>Quiz</li><li><span class="mark"></span>Endorsement</li></ul>
  <div class="section-head"><h3>Endorsement</h3><span class="save"><svg viewBox="0 0 8 8" fill="none" stroke="#0e78bb"><rect x="1" y="1" width="6" height="6"/><path d="M2.5 1v2h3V1"/></svg>Save Progress</span></div>
  <div class="filters"><span class="field select">All categories<svg viewBox="0 0 8 8" fill="none" stroke="#333"><path d="M2 3l2 2 2-2"/></svg></span><span class="field search">Search<svg viewBox="0 0 8 8" fill="none" stroke="#555"><circle cx="3.5" cy="3.5" r="2.5"/><path d="M5.3 5.3 7 7"/></svg></span><span class="field send">Send Request</span></div>
  <div class="people">
    <div class="person"><i class="check"></i><span class="avatar row" role="img" aria-label="Photo of Lena Ostrova"></span>Lena Ostrova<span class="role">Application Design Capabilities</span><span class="btn-add">Add</span></div>
    <div class="person"><i class="check"></i><span class="avatar row" role="img" aria-label="Photo of Owen Hartley"></span>Owen Hartley<span class="role">UI/UX Designer</span><span class="btn-add">Add</span></div>
    <div class="person"><i class="check"></i><span class="avatar row" role="img" aria-label="Photo of Paul Navarro"></span>Paul Navarro<span class="role">Front-end Developer</span><span class="btn-add">Add</span></div>
    <div class="person"><i class="check"></i><span class="avatar row" role="img" aria-label="Photo of Nora Lindqvist"></span>Nora Lindqvist<span class="role">Cybersecurity Analyst</span><span class="btn-add">Add</span></div>
    <div class="person"><i class="check"></i><span class="avatar row" role="img" aria-label="Photo of Simon Avery"></span>Simon Avery<span class="role">DevOps Engineer</span><span class="btn-add">Add</span></div>
    <div class="person"><i class="check"></i><span class="avatar row" role="img" aria-label="Photo of Tessa Morrow"></span>Tessa Morrow<span class="role">DevOps Engineer</span><span class="btn-add">Add</span></div>
    <div class="person"><i class="check"></i><span class="avatar row" role="img" aria-label="Photo of Ivan Beckett"></span>Ivan Beckett<span class="role">DevOps Engineer</span><span class="btn-add">Add</span></div>
  </div>
  <aside class="note"><h4>Note</h4><p>Lorem ipsum dolor sit amet, consecteteur adispiscing elit. Lorem ipsum dolor sit amet, consecteteur adispiscing elit.Lorem ipsum dolor.</p></aside>
  <div class="pager"><span class="pg prev">‹ Previous</span><span class="pg cur">1</span><span>2</span><span class="pg next">Next ›</span></div>
  <footer class="foot"><span class="btn-back">Go Back</span><span class="skip">Skip ›</span><span class="btn-next">Next</span></footer>
  <div class="veil"></div>
  <div class="modal">
    <h4>Endorsements</h4>
    <span class="avatar sm" role="img" aria-label="Photo of selected colleague"></span>
    <p>You will add <b>1</b> colleagues to endorsement you.</p>
    <label>Effective Date</label>
    <span class="field">Select date<svg viewBox="0 0 8 8" fill="none" stroke="#333"><path d="M2 3l2 2 2-2"/></svg></span>
    <div class="modal-actions"><span class="m-cancel">Cancel</span><span class="m-submit">Submit</span></div>
  </div>
</section>

<!-- Screen 4: request sent, ready to submit -->
<section class="screen" style="left:78px;top:612px">
  <header class="nav"><span class="brand"><i class="brand-dot"></i>Veranth</span><nav class="links"><a class="on">Assessments</a><a>Colleagues</a><a>Results</a></nav><span class="nav-icons"><svg viewBox="0 0 10 10" fill="none" stroke="#fff"><path d="M2.5 7V4.5a2.5 2.5 0 0 1 5 0V7l1 1h-7zM4 9h2"/></svg><svg viewBox="0 0 10 10" fill="none" stroke="#fff"><circle cx="5" cy="5" r="3.5"/><circle cx="5" cy="5" r="1.3"/></svg><span class="avatar sm" role="img" aria-label="Profile photo of Mara T. Solvang"></span></span></header>
  <div class="crumb"><svg viewBox="0 0 10 10" fill="none" stroke="#0e78bb"><circle cx="5" cy="5" r="4.3"/><path d="M5.5 3 3.5 5l2 2M3.5 5H7"/></svg><a>Assessment</a>/<span>Application Design Capabilities</span></div>
  <h1 class="a-title"><svg viewBox="0 0 12 12" fill="none" stroke="#333"><rect x="1.5" y="1" width="8" height="10" rx="1"/><path d="M3.5 4h4M3.5 6.5h2"/></svg>UI/UX Designer Assessment</h1>
  <p class="pct">100<small>%</small></p>
  <div class="progress"><i style="width:100%"></i></div>
  <div class="meta"><span>Assessment Date: <a>Feb 12, 2024</a></span><span>Assessment Type: <a>UI/UX Skill</a></span><span>Due Date: 17/02/2024</span><span class="upd">Last Updated: 23/05/2024</span></div>
  <ul class="steps"><li class="done"><span class="mark">✓</span>Quiz</li><li><span class="mark"></span>Endorsement</li></ul>
  <div class="section-head"><h3>Endorsement</h3><span class="save"><svg viewBox="0 0 8 8" fill="none" stroke="#0e78bb"><rect x="1" y="1" width="6" height="6"/><path d="M2.5 1v2h3V1"/></svg>Save Progress</span></div>
  <div class="filters"><span class="field select">All categories<svg viewBox="0 0 8 8" fill="none" stroke="#333"><path d="M2 3l2 2 2-2"/></svg></span><span class="field search">Search<svg viewBox="0 0 8 8" fill="none" stroke="#555"><circle cx="3.5" cy="3.5" r="2.5"/><path d="M5.3 5.3 7 7"/></svg></span><span class="field send">Send Request</span></div>
  <div class="people">
    <div class="person"><i class="check"></i><span class="avatar row" role="img" aria-label="Photo of Lena Ostrova"></span>Lena Ostrova<span class="role">Application Design Capabilities</span><span class="btn-add">Add</span></div>
    <div class="person"><i class="check"></i><span class="avatar row" role="img" aria-label="Photo of Owen Hartley"></span>Owen Hartley<span class="role">UI/UX Designer</span><span class="btn-add">Add</span></div>
    <div class="person"><i class="check"></i><span class="avatar row" role="img" aria-label="Photo of Paul Navarro"></span>Paul Navarro<span class="role">Front-end Developer</span><span class="btn-add">Add</span></div>
    <div class="person"><i class="check"></i><span class="avatar row" role="img" aria-label="Photo of Nora Lindqvist"></span>Nora Lindqvist<span class="role">Cybersecurity Analyst</span><span class="btn-add">Add</span></div>
    <div class="person"><i class="check"></i><span class="avatar row" role="img" aria-label="Photo of Simon Avery"></span>Simon Avery<span class="role" style="margin-right:6px">DevOps Engineer</span><span class="btn-cancel">Cancel</span></div>
    <div class="person"><i class="check"></i><span class="avatar row" role="img" aria-label="Photo of Tessa Morrow"></span>Tessa Morrow<span class="role">DevOps Engineer</span><span class="btn-add">Add</span></div>
    <div class="person"><i class="check"></i><span class="avatar row" role="img" aria-label="Photo of Ivan Beckett"></span>Ivan Beckett<span class="role">DevOps Engineer</span><span class="btn-add">Add</span></div>
  </div>
  <aside class="note"><h4>Note</h4><p>Lorem ipsum dolor sit amet, consecteteur adispiscing elit. Lorem ipsum dolor sit amet, consecteteur adispiscing elit.Lorem ipsum dolor.</p></aside>
  <div class="pager"><span class="pg prev">‹ Previous</span><span class="pg cur">1</span><span>2</span><span class="pg next">Next ›</span></div>
  <footer class="foot"><span class="btn-back">Go Back</span><span class="btn-next">Submit Assessment</span></footer>
</section>

<!-- Screen 5: dashboard after submit -->
<section class="screen" style="left:568.6px;top:612px">
  <header class="nav"><span class="brand"><i class="brand-dot"></i>Veranth</span><nav class="links"><a class="on">Assessments</a><a>Colleagues</a><a>Results</a></nav><span class="nav-icons"><svg viewBox="0 0 10 10" fill="none" stroke="#fff"><path d="M2.5 7V4.5a2.5 2.5 0 0 1 5 0V7l1 1h-7zM4 9h2"/></svg><svg viewBox="0 0 10 10" fill="none" stroke="#fff"><circle cx="5" cy="5" r="3.5"/><circle cx="5" cy="5" r="1.3"/></svg><span class="avatar sm" role="img" aria-label="Profile photo of Mara T. Solvang"></span></span></header>
  <div class="toast"><i>✓</i>The assessment has been successfully submitted.</div>
  <div class="hero">
    <div class="welcome"><span class="avatar lg" role="img" aria-label="Profile photo of Mara T. Solvang"></span><div><p class="hello">Welcome back!</p><p class="who">Mara T. Solvang</p></div><span class="btn-create"><svg viewBox="0 0 8 8" fill="none" stroke="#fff"><rect x="1" y="1" width="6" height="6"/></svg>Create New Assessment</span></div>
    <p class="summary">Summary</p>
    <div class="stats">
      <div class="stat"><svg viewBox="0 0 16 16" fill="none" stroke="#fff"><rect x="2.5" y="1.5" width="10" height="13" rx="1"/><path d="M5 5h5M5 8h3"/><circle cx="10.5" cy="11" r="2"/></svg><div><b>7</b><span>My Assessments</span><small>3 pending</small></div></div>
      <div class="stat"><svg viewBox="0 0 16 16" fill="none" stroke="#fff"><path d="M2 14h12M4 14V9h3l2 2h3v3M8 2v4M6 4l2-2 2 2"/></svg><div><b>4</b><span>Endorsements</span><small>1 pending</small></div></div>
      <div class="stat"><svg viewBox="0 0 16 16" fill="none" stroke="#fff"><circle cx="5.5" cy="5" r="2"/><circle cx="10.5" cy="5" r="2"/><path d="M2 13c0-3 7-3 7 0M7 13c0-3 7-3 7 0"/></svg><div><b>11</b><span>Colleagues</span><small>Last updated on May 23, 2024</small></div></div>
      <div class="stat"><svg viewBox="0 0 16 16" fill="none" stroke="#fff"><path d="M2 9v5h12V9M8 2v8M5 5l3-3 3 3"/></svg><div><b>7</b><span>Submissions</span><small>Last submit on May 23, 2024</small></div></div>
    </div>
  </div>
  <div class="list-area">
    <h2>Assessments</h2>
    <div class="toolbar"><div class="tabs"><span class="tab on">Pending 2</span><span class="tab">Completed 5</span></div><span class="views"><svg viewBox="0 0 10 10" fill="none" stroke="#0e78bb"><path d="M1 2h1M3.5 2H9M1 5h1M3.5 5H9M1 8h1M3.5 8H9"/></svg><svg viewBox="0 0 10 10" fill="none" stroke="#888"><rect x="1" y="1" width="3.3" height="3.3"/><rect x="5.7" y="1" width="3.3" height="3.3"/><rect x="1" y="5.7" width="3.3" height="3.3"/><rect x="5.7" y="5.7" width="3.3" height="3.3"/></svg></span></div>
    <div class="cards">
      <article class="card"><div class="card-id">1723091983<span class="kebab">⋮</span></div><p class="card-title">Application Design Capabilities</p><div class="dates"><div><small>Published on</small><span>20/05/2024</span></div><div><small>Due date</small><span>24/05/2024</span></div></div><div class="chips"><span class="chip">Quiz</span><span class="chip">Endorsement</span><span class="chip">Submission</span></div></article>
      <article class="card"><div class="card-id">1723091983<span class="kebab">⋮</span></div><p class="card-title">Sales Representative Assessments</p><div class="dates"><div><small>Published on</small><span>20/05/2024</span></div><div><small>Due date</small><span>24/05/2024</span></div></div><div class="chips"><span class="chip done">Quiz</span><span class="chip done">Endorsement</span><span class="chip">Submission</span></div></article>
    </div>
  </div>
</section>

<!-- Screen 6: completed list -->
<section class="screen" style="left:78px;top:892px">
  <header class="nav"><span class="brand"><i class="brand-dot"></i>Veranth</span><nav class="links"><a class="on">Assessments</a><a>Colleagues</a><a>Results</a></nav><span class="nav-icons"><svg viewBox="0 0 10 10" fill="none" stroke="#fff"><path d="M2.5 7V4.5a2.5 2.5 0 0 1 5 0V7l1 1h-7zM4 9h2"/></svg><svg viewBox="0 0 10 10" fill="none" stroke="#fff"><circle cx="5" cy="5" r="3.5"/><circle cx="5" cy="5" r="1.3"/></svg><span class="avatar sm" role="img" aria-label="Profile photo of Mara T. Solvang"></span></span></header>
  <div class="hero">
    <div class="welcome"><span class="avatar lg" role="img" aria-label="Profile photo of Mara T. Solvang"></span><div><p class="hello">Welcome back!</p><p class="who">Mara T. Solvang</p></div><span class="btn-create"><svg viewBox="0 0 8 8" fill="none" stroke="#fff"><rect x="1" y="1" width="6" height="6"/></svg>Create New Assessment</span></div>
    <p class="summary">Summary</p>
    <div class="stats">
      <div class="stat"><svg viewBox="0 0 16 16" fill="none" stroke="#fff"><rect x="2.5" y="1.5" width="10" height="13" rx="1"/><path d="M5 5h5M5 8h3"/><circle cx="10.5" cy="11" r="2"/></svg><div><b>7</b><span>My Assessments</span><small>3 pending</small></div></div>
      <div class="stat"><svg viewBox="0 0 16 16" fill="none" stroke="#fff"><path d="M2 14h12M4 14V9h3l2 2h3v3M8 2v4M6 4l2-2 2 2"/></svg><div><b>3</b><span>Endorsements</span><small>1 pending</small></div></div>
      <div class="stat"><svg viewBox="0 0 16 16" fill="none" stroke="#fff"><circle cx="5.5" cy="5" r="2"/><circle cx="10.5" cy="5" r="2"/><path d="M2 13c0-3 7-3 7 0M7 13c0-3 7-3 7 0"/></svg><div><b>10</b><span>Colleagues</span><small>Last updated on May 23, 2024</small></div></div>
      <div class="stat"><svg viewBox="0 0 16 16" fill="none" stroke="#fff"><path d="M2 9v5h12V9M8 2v8M5 5l3-3 3 3"/></svg><div><b>7</b><span>Submissions</span><small>Last submit on May 23, 2024</small></div></div>
    </div>
  </div>
  <div class="list-area">
    <h2>Assessments</h2>
    <div class="toolbar"><div class="tabs"><span class="tab">Pending 2</span><span class="tab on">Completed 5</span></div><span class="views"><svg viewBox="0 0 10 10" fill="none" stroke="#0e78bb"><path d="M1 2h1M3.5 2H9M1 5h1M3.5 5H9M1 8h1M3.5 8H9"/></svg><svg viewBox="0 0 10 10" fill="none" stroke="#888"><rect x="1" y="1" width="3.3" height="3.3"/><rect x="5.7" y="1" width="3.3" height="3.3"/><rect x="1" y="5.7" width="3.3" height="3.3"/><rect x="5.7" y="5.7" width="3.3" height="3.3"/></svg></span></div>
    <div class="cards">
      <article class="card"><div class="card-id">1723091983<span class="kebab">⋮</span></div><p class="card-title">UI/UX Designer Assessments</p><div class="dates"><div><small>Published on</small><span>20/05/2024</span></div><div><small>Due date</small><span>24/05/2024</span></div></div><div class="chips"><span class="chip done">Quiz</span><span class="chip done">Endorsement</span></div></article>
      <article class="card"><div class="card-id">1723091983<span class="kebab">⋮</span></div><p class="card-title">Front-end Developer Assessments</p><div class="dates"><div><small>Published on</small><span>20/05/2024</span></div><div><small>Due date</small><span>24/05/2024</span></div></div><div class="chips"><span class="chip done">Endorsement</span><span class="chip done">Submission</span></div></article>
      <article class="card"><div class="card-id">1723091983<span class="kebab">⋮</span></div><p class="card-title">Cybersecurity Analyst Assessments</p><div class="dates"><div><small>Published on</small><span>20/05/2024</span></div><div><small>Due date</small><span>24/05/2024</span></div></div><div class="chips"><span class="chip done">Quiz</span></div></article>
      <article class="card"><div class="card-id">1723091983<span class="kebab">⋮</span></div><p class="card-title">DevOps Engineer Assessments</p><div class="dates"><div><small>Published on</small><span>20/05/2024</span></div><div><small>Due date</small><span>24/05/2024</span></div></div><div class="chips"><span class="chip done">Quiz</span><span class="chip done">Endorsement</span><span class="chip done">Submission</span></div></article>
      <article class="card"><div class="card-id">1723091983<span class="kebab">⋮</span></div><p class="card-title">Sales Representative Assessments</p><div class="dates"><div><small>Published on</small><span>20/05/2024</span></div><div><small>Due date</small><span>24/05/2024</span></div></div><div class="chips"><span class="chip done">Quiz</span><span class="chip done">Endorsement</span></div></article>
    </div>
  </div>
</section>

<!-- Screen 7: completed list with card menu -->
<section class="screen" style="left:568.6px;top:892px">
  <header class="nav"><span class="brand"><i class="brand-dot"></i>Veranth</span><nav class="links"><a class="on">Assessments</a><a>Colleagues</a><a>Results</a></nav><span class="nav-icons"><svg viewBox="0 0 10 10" fill="none" stroke="#fff"><path d="M2.5 7V4.5a2.5 2.5 0 0 1 5 0V7l1 1h-7zM4 9h2"/></svg><svg viewBox="0 0 10 10" fill="none" stroke="#fff"><circle cx="5" cy="5" r="3.5"/><circle cx="5" cy="5" r="1.3"/></svg><span class="avatar sm" role="img" aria-label="Profile photo of Mara T. Solvang"></span></span></header>
  <div class="hero">
    <div class="welcome"><span class="avatar lg" role="img" aria-label="Profile photo of Mara T. Solvang"></span><div><p class="hello">Welcome back!</p><p class="who">Mara T. Solvang</p></div><span class="btn-create"><svg viewBox="0 0 8 8" fill="none" stroke="#fff"><rect x="1" y="1" width="6" height="6"/></svg>Create New Assessment</span></div>
    <p class="summary">Summary</p>
    <div class="stats">
      <div class="stat"><svg viewBox="0 0 16 16" fill="none" stroke="#fff"><rect x="2.5" y="1.5" width="10" height="13" rx="1"/><path d="M5 5h5M5 8h3"/><circle cx="10.5" cy="11" r="2"/></svg><div><b>7</b><span>My Assessments</span><small>3 pending</small></div></div>
      <div class="stat"><svg viewBox="0 0 16 16" fill="none" stroke="#fff"><path d="M2 14h12M4 14V9h3l2 2h3v3M8 2v4M6 4l2-2 2 2"/></svg><div><b>3</b><span>Endorsements</span><small>1 pending</small></div></div>
      <div class="stat"><svg viewBox="0 0 16 16" fill="none" stroke="#fff"><circle cx="5.5" cy="5" r="2"/><circle cx="10.5" cy="5" r="2"/><path d="M2 13c0-3 7-3 7 0M7 13c0-3 7-3 7 0"/></svg><div><b>10</b><span>Colleagues</span><small>Last updated on May 23, 2024</small></div></div>
      <div class="stat"><svg viewBox="0 0 16 16" fill="none" stroke="#fff"><path d="M2 9v5h12V9M8 2v8M5 5l3-3 3 3"/></svg><div><b>7</b><span>Submissions</span><small>Last submit on May 23, 2024</small></div></div>
    </div>
  </div>
  <div class="list-area">
    <h2>Assessments</h2>
    <div class="toolbar"><div class="tabs"><span class="tab">Pending 2</span><span class="tab on">Completed 5</span></div><span class="views"><svg viewBox="0 0 10 10" fill="none" stroke="#0e78bb"><path d="M1 2h1M3.5 2H9M1 5h1M3.5 5H9M1 8h1M3.5 8H9"/></svg><svg viewBox="0 0 10 10" fill="none" stroke="#888"><rect x="1" y="1" width="3.3" height="3.3"/><rect x="5.7" y="1" width="3.3" height="3.3"/><rect x="1" y="5.7" width="3.3" height="3.3"/><rect x="5.7" y="5.7" width="3.3" height="3.3"/></svg></span></div>
    <div class="cards">
      <article class="card"><div class="card-id">1723091983<span class="kebab">⋮</span></div><p class="card-title">UI/UX Designer Assessments</p><div class="dates"><div><small>Published on</small><span>20/05/2024</span></div><div><small>Due date</small><span>24/05/2024</span></div></div><div class="chips"><span class="chip done">Quiz</span><span class="chip done">Endorsement</span></div><div class="menu"><div>Edit</div><div>Delete</div><div>Review</div></div></article>
      <article class="card"><div class="card-id">1723091983<span class="kebab">⋮</span></div><p class="card-title">Front-end Developer Assessments</p><div class="dates"><div><small>Published on</small><span>20/05/2024</span></div><div><small>Due date</small><span>24/05/2024</span></div></div><div class="chips"><span class="chip done">Endorsement</span><span class="chip done">Submission</span></div></article>
      <article class="card"><div class="card-id">1723091983<span class="kebab">⋮</span></div><p class="card-title">Cybersecurity Analyst Assessments</p><div class="dates"><div><small>Published on</small><span>20/05/2024</span></div><div><small>Due date</small><span>24/05/2024</span></div></div><div class="chips"><span class="chip done">Quiz</span></div></article>
      <article class="card"><div class="card-id">1723091983<span class="kebab">⋮</span></div><p class="card-title">DevOps Engineer Assessments</p><div class="dates"><div><small>Published on</small><span>20/05/2024</span></div><div><small>Due date</small><span>24/05/2024</span></div></div><div class="chips"><span class="chip done">Quiz</span><span class="chip done">Endorsement</span><span class="chip done">Submission</span></div></article>
      <article class="card"><div class="card-id">1723091983<span class="kebab">⋮</span></div><p class="card-title">Sales Representative Assessments</p><div class="dates"><div><small>Published on</small><span>20/05/2024</span></div><div><small>Due date</small><span>24/05/2024</span></div></div><div class="chips"><span class="chip done">Quiz</span><span class="chip done">Endorsement</span></div></article>
    </div>
  </div>
</section>

</main>
</body>
</html>
```